Business card for a boutique travel agency VELARIEN

we need a business card design - double sided. We would like to have a very elegant, sophisticated but modern design. we are travel consultants and our business focus is Europe, mainly the city of Paris. We would like to receive designs in white and silver, black color but if you are confident that we should pick up a color to make it different and more beautful...go ahead! We are going to give business cards to our clients and business partners. It is important to be perceived as elegant, modern and trustful. Please check jpg references.

Target Market(s)

Velarien primary clients are individuals, couples and affinity groups of high-net-worth who travel for leisure at least once per year. Seeking the ultimate travel experience, the target clients demand the finest quality activities and accommodations accompanied by a superior level of service.

Industry/Entity Type

Travel Industry

Contact Information for Business Card

Lucinda Farrow
- lucinda@velarien-example.com
- +55 11 98347.2516
- velarien-example.com
- unique travel experiences (we would like to see this signature printed as a detail)

Font styles to use
Sans Serif

Colors

Designer to choose colors to be used in the design.

Requirements
Must have
• the Velarien logo that I have attached
Nice to have
• we would like to have some nice detail, something different that shows that we care about,... we are detail oriented.
Should not have
• decorative fonts

```html
<!DOCTYPE html>
<html lang="en">
<head>
<meta charset="UTF-8">
<title>Velarien — Business Card</title>
<link rel="stylesheet" href="https://fonts.googleapis.com/css2?family=Josefin+Sans:wght@300;400&display=swap">
<style>
  :root {
    --backdrop: #3a3a3a;
    --card: #1f1f20;
    --mark-area-light: #3b3b3d;
    --mark-area-dark: #1f1f20;
    --ink: #f4f4f4;
    --ink-soft: #d9d9d9;
    --ink-muted: #a8a8a8;
  }
  html, body {
    margin: 0;
    padding: 0;
    width: 799px;
    height: 1200px;
    overflow: hidden;
    background: var(--backdrop);
    font-family: "Josefin Sans", sans-serif;
  }
  .sheet {
    position: relative;
    width: 799px;
    height: 1200px;
  }
  .card {
    position: absolute;
    left: 90px;
    width: 620px;
    height: 354px;
    background: var(--card);
    box-shadow: 0 14px 30px rgba(0,0,0,0.45);
    color: var(--ink);
    overflow: hidden;
  }
  .card--front { top: 125px; }
  .card--back  { top: 720px; }

  .mark-area {
    position: absolute;
    background: radial-gradient(circle at 50% 50%, var(--mark-area-light) 0%, var(--mark-area-dark) 70%);
  }
  .card--front .mark-area {
    left: 210px;
    top: 57px;
    width: 220px;
    height: 240px;
  }
  .card--back .mark-area {
    left: 0;
    top: 0;
    width: 250px;
    height: 354px;
  }

  .wordmark {
    position: absolute;
    font-weight: 400;
    letter-spacing: 0.42em;
    white-space: nowrap;
    color: var(--ink);
  }
  .card--front .wordmark {
    top: 150px;
    left: 0;
    width: 100%;
    text-align: center;
    font-size: 40px;
    padding-left: 0.42em;
    box-sizing: border-box;
  }
  .tagline {
    position: absolute;
    left: 0;
    width: 100%;
    bottom: 34px;
    margin: 0;
    text-align: center;
    font-size: 12px;
    font-weight: 300;
    letter-spacing: 0.35em;
    text-transform: lowercase;
    color: var(--ink-muted);
  }
  .card--back .wordmark {
    top: 70px;
    right: 40px;
    font-size: 24px;
  }
  .holder {
    position: absolute;
    left: 280px;
    top: 186px;
  }
  .holder__name {
    margin: 0 0 14px;
    font-size: 22px;
    font-weight: 400;
    letter-spacing: 0.08em;
    text-transform: uppercase;
  }
  .holder__contact {
    margin: 0;
    padding: 0;
    list-style: none;
    font-size: 14px;
    font-weight: 300;
    line-height: 1.55;
    color: var(--ink-soft);
  }
</style>
</head>
<body>
  <main class="sheet">
    <section class="card card--front" aria-label="Card front">
      <div class="mark-area" role="img" aria-label="Brand symbol placed behind the name"></div>
      <div class="wordmark">VELARIEN</div>
      <p class="tagline">unique travel experiences</p>
    </section>

    <section class="card card--back" aria-label="Card back">
      <div class="mark-area" role="img" aria-label="Large brand symbol on the left edge"></div>
      <div class="wordmark">VELARIEN</div>
      <div class="holder">
        <h1 class="holder__name">Lucinda Farrow</h1>
        <ul class="holder__contact">
          <li>+55 11 98347.2516</li>
          <li>lucinda@velarien-example.com</li>
          <li>www.velarien-example.com</li>
        </ul>
      </div>
    </section>
  </main>
</body>
</html>
```